Portfolio site - Need a basic WordPress or SquareSpace site

I need a portfolio site where I have the option to keep updating it on my own. Therefore, I'm guessing I need one that uses WordPress or SquareSpace. I just need a simple and elegant design. I'm a writer (scholarly, fiction and journalism).

Target Market(s)

Adult

Industry/Entity Type

Writer

Number of Pages Required

4 page

Font styles to use
Serif

Colors
b7a5cd
e667a6
85abd2

Requirements
Must have
• Easily updatable features. I'll have to publish links and small blurbs from time to time. And maybe the occasional image.
• Pages should be:
• Home
• Work
• Press
• Contact

```html
<!DOCTYPE html>
<html lang="en">
<head>
<meta charset="utf-8">
<title>Mariam Aldine — Writer</title>
<link rel="stylesheet" href="https://fonts.googleapis.com/css2?family=Playfair+Display:wght@700&family=Jost:wght@400;500&family=Lato:wght@400;700&display=swap">
<style>
:root{
  --plum:#5a4266;
  --plum-dark:#4a3456;
  --lilac:#b7a5cd;
  --lilac-mid:#9c87b6;
  --pink:#e667a6;
  --blue:#85abd2;
  --ink:#3b2a47;
  --text:#555;
  --grey-bg:#f3f3f3;
  --white:#fff;
  --title-blue:#1f6a9a;
}
*{box-sizing:border-box;margin:0;padding:0}
html,body{width:1200px;height:3495px;overflow:hidden}
body{position:relative;background:var(--white);font-family:"Lato",sans-serif;color:var(--text)}
.abs{position:absolute}
.circle-link{width:44px;height:44px;border-radius:50%;border:2px solid #bbb;display:inline-block;margin-right:8px}
.circle-link.filled{background:var(--plum);border-color:var(--plum)}

/* header */
.site-header{left:0;top:0;width:1200px;height:124px}
.site-header .social{left:77px;top:32px}
.brand{left:0;width:1200px;top:40px;text-align:center;font-family:"Playfair Display",serif;font-size:34px;color:var(--ink)}
.brand-dot{display:inline-block;width:14px;height:14px;border-radius:50%;background:var(--lilac);margin-left:10px;vertical-align:middle}
.header-mail{right:77px;top:50px;font-size:18px;color:var(--text);display:flex;align-items:center;gap:10px}

/* nav */
.main-nav{left:0;top:124px;width:1200px;height:63px;background:var(--plum);display:flex;justify-content:center;padding-left:30px}
.main-nav a{color:var(--white);text-decoration:none;font-family:"Jost",sans-serif;font-size:18px;line-height:63px;padding:0 32px;margin:0 6px}
.main-nav a.active{background:var(--lilac-mid)}

/* hero */
.hero{left:0;top:187px;width:1200px;height:575px;overflow:hidden;background:var(--plum)}
.hero svg{position:absolute;left:0;top:0}
.hero-card{left:77px;top:79px;width:468px;height:417px;background:var(--white);box-shadow:0 4px 14px rgba(0,0,0,.25);padding:44px 40px;text-align:center}
.hero-card::after{content:"";position:absolute;right:-22px;top:170px;border-left:22px solid var(--white);border-top:22px solid transparent;border-bottom:22px solid transparent}
.hero-card h1{font-family:"Playfair Display",serif;font-size:44px;line-height:1.15;color:var(--ink);margin-bottom:24px}
.hero-card p{font-size:17px;line-height:1.95;color:#555}
.hero-photo{left:664px;top:20px;width:431px;height:555px;background:linear-gradient(180deg,#c9a58a,#3f5f8f 70%,#2f4d78);border-radius:200px 200px 0 0}

/* book carousel */
.books{left:0;top:762px;width:1200px;height:333px}
.book{position:absolute;top:63px;width:140px;height:207px}
.arrow{position:absolute;top:131px;width:46px;height:46px;border-radius:50%}

/* about */
.about{left:0;top:1095px;width:1200px;height:419px;background:linear-gradient(100deg,var(--lilac) 0%,#7a6090 35%,var(--plum) 70%,var(--plum-dark));text-align:center;color:var(--white)}
.section-title{font-family:"Jost",sans-serif;font-weight:500;font-size:38px;display:flex;align-items:center;justify-content:center;gap:40px}
.section-title::before,.section-title::after{content:"";width:100px;height:1px;background:currentColor;opacity:.5}
.about .section-title{margin-top:60px}
.about p{width:800px;margin:30px auto 0;font-size:14.5px;line-height:1.95}
.btn{display:inline-block;font-family:"Jost",sans-serif;font-size:18px;padding:0 30px;line-height:62px;text-decoration:none}
.btn-light{background:var(--white);color:var(--ink);margin-top:34px;padding:0 36px}
.btn-dark{background:var(--plum);color:var(--white)}

/* feature */
.feature{left:0;top:1514px;width:1200px;height:497px}
.feature-cover{left:77px;top:70px;width:233px;height:368px;background:linear-gradient(135deg,#2b3a4a,#3d6e7e 50%,#a8412e);box-shadow:6px 6px 14px rgba(0,0,0,.35)}
.feature-body{left:380px;top:66px;width:745px}
.feature-body h2{font-family:"Jost",sans-serif;font-weight:500;font-size:37px;line-height:1.25;color:var(--ink);margin-bottom:22px}
.feature-body p{font-size:14.5px;line-height:1.95;margin-bottom:18px}
.feature-body .btn{margin-top:6px}

/* articles */
.articles{left:0;top:2011px;width:1200px;height:710px;background:var(--grey-bg)}
.articles .section-title{color:var(--ink);margin-top:58px;font-size:38px}
.articles .section-title::before,.articles .section-title::after{background:#999}
.card{position:absolute;top:149px;width:333px;height:480px;background:var(--white);box-shadow:0 1px 5px rgba(0,0,0,.15);text-align:center}
.card-image{height:192px}
.avatar{position:absolute;left:28px;top:160px;width:70px;height:70px;border-radius:50%;border:3px solid var(--white);background:linear-gradient(#8a6a52,#3a2a25)}
.card-date{margin:16px 0 0 90px;font-size:14px;font-style:italic;color:#777;text-align:left;padding-left:20px}
.card-rule{height:1px;background:#ddd;margin:14px 30px 0 110px}
.card h3{font-family:"Jost",sans-serif;font-weight:500;font-size:19px;color:var(--title-blue);margin-top:26px}
.card p{font-size:15px;line-height:1.9;padding:0 36px;margin-top:14px}
.card .btn{margin-top:18px;font-size:16px;line-height:52px;padding:0 26px}

/* subscribe */
.subscribe{left:0;top:2721px;width:1200px;height:513px;background:linear-gradient(180deg,#b9bcc3,#8f8f95 45%,#d8c7ad 60%,#6d6e78)}
.subscribe-box{left:77px;top:87px;width:1046px;height:342px;background:rgba(255,255,255,.55);text-align:center;color:var(--ink)}
.subscribe-box .section-title{margin-top:40px;font-size:38px}
.subscribe-box .section-title::before,.subscribe-box .section-title::after{background:var(--ink)}
.subscribe-box p{width:700px;margin:18px auto 0;font-size:15px;line-height:1.9}
.signup{display:flex;justify-content:center;gap:20px;margin-top:34px}
.signup input{width:470px;height:72px;border:0;padding:0 14px;font-size:14px;font-family:"Lato",sans-serif}
.signup button{width:146px;height:72px;border:0;background:var(--plum);color:var(--white);font-family:"Jost",sans-serif;font-size:19px}

/* footer */
.site-footer{left:0;top:3234px;width:1200px;height:261px;background:linear-gradient(100deg,var(--lilac) 0%,#7a6090 40%,var(--plum) 75%,var(--plum-dark));text-align:center;color:var(--white)}
.site-footer .social{margin-top:82px}
.site-footer .circle-link{border-color:rgba(255,255,255,.6);margin:0 4px}
.site-footer .circle-link.filled{background:var(--white);border-color:var(--white)}
.copyright{margin-top:34px;font-size:14px}
.copyright strong{font-weight:700}
</style>
</head>
<body>

<header class="site-header abs">
  <div class="social abs"><span class="circle-link filled"></span><span class="circle-link"></span><span class="circle-link"></span></div>
  <div class="brand abs">Mariam Aldine<span class="brand-dot"></span></div>
  <div class="header-mail abs">
    <svg width="24" height="17" viewBox="0 0 24 17"><rect width="24" height="17" rx="2" fill="#e667a6"/><path d="M1 2l11 8 11-8" stroke="#fff" stroke-width="2" fill="none"/></svg>
    me@mariamaldine.com
  </div>
</header>

<nav class="main-nav abs">
  <a href="#" class="active">HOME</a><a href="#">ABOUT</a><a href="#">WORK</a><a href="#">PRESS</a><a href="#">CONTACT</a>
</nav>

<section class="hero abs">
  <svg width="1200" height="575" viewBox="0 0 1200 575">
    <rect width="1200" height="575" fill="#7c5f8c"/>
    <polygon points="0,0 470,0 560,150 0,320" fill="#e667a6"/>
    <polygon points="470,0 1200,0 1200,80 640,200" fill="#6c5080"/>
    <polygon points="0,320 560,150 660,575 0,575" fill="#85abd2"/>
    <polygon points="560,150 1200,80 1200,575 660,575" fill="#75598a"/>
    <polygon points="0,575 0,420 330,575" fill="#b7a5cd"/>
  </svg>
  <div class="hero-photo abs" role="img" aria-label="Portrait photo of the writer smiling with thumbs up"></div>
  <div class="hero-card abs">
    <h1>Hi, I'm Mariam Aldine</h1>
    <p>Lorem Ipsum is simply dummy text of the printing and typesetting industry. Lorem Ipsum has been the industry's standard dummy text ever since the 1500s, when an unknown printer took a galley of type and scrambled it to make a type specimen book.</p>
  </div>
</section>

<section class="books abs">
  <svg class="arrow" style="left:53px" viewBox="0 0 46 46"><circle cx="23" cy="23" r="23" fill="#b7a5cd"/><path d="M26 15l-8 8 8 8" stroke="#fff" stroke-width="3" fill="none"/></svg>
  <div class="book" style="left:133px;background:linear-gradient(#b9e0d8,#8f6bb0)" role="img" aria-label="Book cover: comic anthology"></div>
  <div class="book" style="left:291px;background:linear-gradient(#3c6aa6 0,#f3f0e6 30%,#7e8c7a)" role="img" aria-label="Book cover: travel memoir"></div>
  <div class="book" style="left:450px;background:linear-gradient(#6f7a4e,#c7b57a)" role="img" aria-label="Book cover: novel with kitchen scene"></div>
  <div class="book" style="left:608px;background:linear-gradient(#1d2a30,#3f6a5e)" role="img" aria-label="Book cover: novel with butterflies"></div>
  <div class="book" style="left:769px;background:linear-gradient(#1d2d44,#e07a2a)" role="img" aria-label="Book cover: fantasy adventure"></div>
  <div class="book" style="left:927px;background:linear-gradient(#2d6e8a,#f0a030 60%,#c84a20)" role="img" aria-label="Book cover: novel with sunset tree"></div>
  <svg class="arrow" style="left:1101px" viewBox="0 0 46 46"><circle cx="23" cy="23" r="23" fill="#e667a6"/><path d="M20 15l8 8-8 8" stroke="#fff" stroke-width="3" fill="none"/></svg>
</section>

<section class="about abs">
  <h2 class="section-title">About Mariam Aldine</h2>
  <p>Mariam Aldine is a writer and comics scholar. She recently published her first short story comic, "1001 Lakeshore Nights" in the Harbourfront Hearts Anthology which was illustrated by Lena Corvit. As a comics scholar, her research interests are mainly focused on Muslimah and intersectional superheroes, as well as racialized women in comics. She most recently completed an audience analysis of young adult Muslim consumers of comics, and is currently working on more fiction and scholarly projects. She lives in Toronto, Ontario.</p>
  <a href="#" class="btn btn-light">READ MORE</a>
</section>

<section class="feature abs">
  <div class="feature-cover abs" role="img" aria-label="Anthology book cover with illustrated city scene"></div>
  <div class="feature-body abs">
    <h2>The Lakeshore Comics anthology series showcases rising talent</h2>
    <p>A trans woman embarks on a quest to find a safe bathroom; residents of the future must fight a robot to purchase a condominium; and clowns rampage in the historic Toronto Circus Riot of 1855 – all within a single, diverse new comics anthology.</p>
    <p>Kessler and a team of colleagues began the Lakeshore Comics series in 2014 after meeting at the comic-book boot camp taught by Rory Fenwick, the Beacon Award–winning artist best known for his work on the Midnight Warden Adventures.</p>
    <a href="#" class="btn btn-dark">READ MORE</a>
  </div>
</section>

<section class="articles abs">
  <h2 class="section-title">Mariam Aldine Articles</h2>
  <article class="card" style="left:77px">
    <div class="card-image" style="background:linear-gradient(135deg,#4a4a55,#b8b6bd 60%,#e6e4e8)" role="img" aria-label="Photo of hands typing on a laptop"></div>
    <div class="avatar" role="img" aria-label="Author avatar"></div>
    <div class="card-date">Posted at 24 July 2018</div><div class="card-rule"></div>
    <h3>LOREM IPSUM SIMPLY DUMY</h3>
    <p>Lorem Ipsum is simply dummy text of the printing and typesetting industry. Lorem Ipsum has been the industry.</p>
    <a href="#" class="btn btn-dark">READ MORE</a>
  </article>
  <article class="card" style="left:433px">
    <div class="card-image" style="background:linear-gradient(180deg,#e9b35a,#f6e2a8 45%,#5a4a30)" role="img" aria-label="Photo of a person in a sunset field with birds"></div>
    <div class="avatar" role="img" aria-label="Author avatar"></div>
    <div class="card-date">Posted at 24 July 2018</div><div class="card-rule"></div>
    <h3>LOREM IPSUM SIMPLY DUMY</h3>
    <p>Lorem Ipsum is simply dummy text of the printing and typesetting industry. Lorem Ipsum has been the industry.</p>
    <a href="#" class="btn btn-dark">READ MORE</a>
  </article>
  <article class="card" style="left:790px">
    <div class="card-image" style="background:linear-gradient(135deg,#f2f2f2,#d6d8dc 60%,#a9adb4)" role="img" aria-label="Photo of a woman writing at an office desk"></div>
    <div class="avatar" role="img" aria-label="Author avatar"></div>
    <div class="card-date">Posted at 24 July 2018</div><div class="card-rule"></div>
    <h3>LOREM IPSUM SIMPLY DUMY</h3>
    <p>Lorem Ipsum is simply dummy text of the printing and typesetting industry. Lorem Ipsum has been the industry.</p>
    <a href="#" class="btn btn-dark">READ MORE</a>
  </article>
</section>

<section class="subscribe abs" role="img" aria-label="Hazy city skyline at sunrise">
  <div class="subscribe-box abs">
    <h2 class="section-title">Subscribe</h2>
    <p>Subscribe to my newsletter for updates on recently published work, my classes, books I'm reading, places I'm visiting and other musings and observations.</p>
    <form class="signup"><input type="email" placeholder="Enter Email"><button type="button">SIGN UP</button></form>
  </div>
</section>

<footer class="site-footer abs">
  <div class="social"><span class="circle-link filled"></span><span class="circle-link"></span><span class="circle-link"></span></div>
  <p class="copyright">© 2017 All Rights Reserved | Site by <strong>MARIAM ALDINE</strong> .</p>
</footer>

</body>
</html>
```